Creating a website for a life changing company (Past Q)

We do need a website for our Coaching and Consulting business we recently launched. We do need it for information purposes and that our clients do have the opportunity to subscribe for packages, programs etc.
We would like to see designs which use the colours blue and yellow (see attachment). The final design should communicate our passion for the potential in people and the benefit (going beyond) for them.
Additional information:
Our company (webpage): Past Q (the C stands for "what people cannot see / imagine now...)
Welcome to Past Q(uarter)
Consulting (R.I.M.) & Coaching (Rise further)
Two pillars:
1) R.I.M. ( Stewardship ascent - Our program - focussing on companies - business orientated)
2) Rise further (Path renewal - Events - focusing on individuals - primarily life changing)
For both of them we offer: Concierge & Past Q+ (This should go as a subscription)
Eventually you can draft this as a rhombus
Industry/Entity Type
Coaching / Consulting
Coding
Coded - Design and coding required
Number of Pages Required
1 page
Font styles to use
Other font styles liked:
- Lato
Requirements
Must have
- Please see attachment (About us / Offers / Calendar function / Links to Instagram and LinkedIn account / mailing list / page for clients
Nice to have
- A banner

```html
<!DOCTYPE html>
<html lang="en">
<head>
<meta charset="utf-8">
<title>Past Q — Life Changing Center</title>
<link rel="stylesheet" href="https://fonts.googleapis.com/css2?family=Lato:wght@400;700;900&family=Montserrat:wght@600;700;800&display=swap">
<style>
:root{
  --blue:#0b4fc4;
  --blue-bright:#1a8cff;
  --blue-deep:#083a96;
  --yellow:#f5c518;
  --yellow-soft:#f7d447;
  --ink:#1b1b1b;
  --text:#555b66;
  --line:#d9dde4;
  --white:#ffffff;
  --black:#050505;
}
*{box-sizing:border-box;margin:0;padding:0}
html,body{width:1200px;height:4592px;overflow:hidden}
body{font-family:'Lato',sans-serif;color:var(--ink);background:var(--white);position:relative}
.abs{position:absolute}
.heading{font-family:'Montserrat',sans-serif;font-weight:800;text-transform:uppercase;letter-spacing:.5px}
.mark{width:46px;height:46px;border-radius:50%;background:var(--yellow);display:inline-block}
.pill{display:inline-flex;align-items:center;justify-content:center;border-radius:30px;font-weight:700;font-size:15px}

/* header */
.site-header{top:0;left:0;width:1200px;height:150px;background:var(--white)}
.brand{left:96px;top:50px;display:flex;align-items:center;gap:12px}
.brand .dot{width:40px;height:40px;border-radius:50%;background:var(--yellow)}
.brand-name{font-family:'Montserrat',sans-serif;font-weight:800;font-size:22px;color:var(--blue-deep);letter-spacing:2px}
.phone-pill{left:942px;top:10px;width:140px;height:34px;background:var(--blue);color:var(--white);font-size:14px;gap:8px}
.main-nav{left:262px;top:74px;display:flex;align-items:center;gap:30px;font-family:'Montserrat',sans-serif;font-weight:700;font-size:13px;color:var(--ink)}
.contact-btn{background:var(--yellow);color:var(--ink);height:40px;width:140px;border-radius:22px;display:flex;align-items:center;justify-content:center;margin-left:6px}

/* hero */
.hero{top:150px;left:0;width:1200px;height:800px;background:linear-gradient(120deg,#3f6b2a 0%,#6f9a3a 35%,#2f5220 60%,#183312 100%)}
.hero-title{right:110px;top:200px;text-align:right;color:var(--white);font-size:56px;line-height:62px}
.hero-text{right:110px;top:352px;width:470px;text-align:right;color:var(--white);font-size:16px;line-height:24px;font-weight:700}
.hero-btn{right:110px;top:446px;width:130px;height:38px;background:var(--white);color:var(--blue)}
.hero-wave{left:0;top:640px;width:1200px;height:170px}

/* welcome */
.welcome-title{left:110px;top:990px;display:flex;align-items:center;gap:14px;font-size:26px}
.welcome-copy{left:110px;top:1075px;width:460px;font-size:15px;line-height:24px;color:var(--text)}
.welcome-copy p+p{margin-top:18px}
.read-btn{left:110px;top:1400px;width:130px;height:36px;background:var(--blue);color:var(--white)}
.portrait{border-radius:14px}
.portrait-a{left:598px;top:1040px;width:238px;height:380px;background:linear-gradient(160deg,#7fa0b8,#4f6e86 55%,#2f4658)}
.portrait-b{left:820px;top:990px;width:270px;height:380px;background:linear-gradient(160deg,#8a94a0,#41566e 55%,#22334a)}
.accent{background:var(--yellow)}
.arrow-tab{width:44px;height:36px;display:flex;align-items:center;justify-content:center;border-radius:6px}

/* consulting */
.consulting{top:1500px;left:0;width:1200px;height:620px;background:linear-gradient(180deg,var(--blue) 0%,var(--blue-bright) 100%)}
.consulting-title{left:0;top:1600px;width:1200px;display:flex;justify-content:center;align-items:center;gap:14px;color:var(--white);font-size:30px}
.consulting-title .mark{background:var(--white)}
.service{width:220px;height:220px;border-radius:50%;background:var(--blue);border:5px solid var(--yellow);color:var(--white);text-align:center;padding-top:40px}
.service svg{display:block;margin:0 auto 10px}
.service h3{font-family:'Montserrat',sans-serif;font-size:14px;font-weight:700}
.service p{font-size:10px;line-height:14px;margin:8px 26px 0;opacity:.9}
.service .tab{position:absolute;left:88px;bottom:-6px;width:44px;height:26px;border-radius:6px 6px 0 0;background:var(--yellow);display:flex;align-items:center;justify-content:center}
.consult-wave{left:0;top:1990px;width:1200px;height:140px}

/* packages */
.packages-title{left:0;top:2130px;width:1200px;text-align:center}
.packages-title h2{font-size:30px;margin-top:14px}
.plan{width:320px;height:420px;border:1px solid var(--line);background:var(--white);text-align:center;box-shadow:0 4px 14px rgba(0,0,0,.06)}
.plan-head{height:54px;background:var(--yellow);display:flex;align-items:center;justify-content:center;font-family:'Montserrat',sans-serif;font-weight:700;font-size:18px}
.price{margin-top:26px;font-family:'Montserrat',sans-serif;font-weight:700;font-size:40px;color:var(--blue)}
.price sup{font-size:16px;vertical-align:18px;margin-right:4px}
.per{font-weight:700;font-size:13px;color:var(--blue);margin-top:2px}
.features{list-style:none;margin-top:20px;font-size:14px;line-height:27px;color:var(--text)}
.features li{border-bottom:1px solid #eef0f3;margin:0 40px}
.plan .sign{position:absolute;left:110px;bottom:-18px;width:100px;height:34px;background:var(--blue);color:var(--white)}

/* rise further */
.yellow-band{left:0;top:2700px;width:1200px;height:860px}
.rise-title{left:0;top:2880px;width:1200px;text-align:center}
.rise-title .mark{background:var(--blue-deep)}
.rise-title h2{font-size:30px;margin-top:14px}
.pillar{width:230px;height:350px;background:var(--white);border-radius:115px 115px 16px 16px;overflow:hidden;text-align:center;box-shadow:0 6px 16px rgba(0,0,0,.1)}
.pillar .photo{height:190px;border-radius:115px 115px 0 0}
.pillar h3{font-family:'Montserrat',sans-serif;font-weight:700;font-size:18px;line-height:22px;height:66px;display:flex;align-items:center;justify-content:center;margin-top:22px;padding:0 16px}
.pillar .go{width:36px;height:36px;border-radius:50%;background:var(--blue);margin:14px auto 0;display:flex;align-items:center;justify-content:center}

/* contact */
.contact-title{left:0;top:3600px;width:1200px;text-align:center}
.contact-title .mark{background:var(--ink)}
.contact-title h2{font-size:32px;margin-top:14px}
.info{left:160px;width:320px;display:flex;gap:20px}
.info svg{flex:none;margin-top:2px}
.info h4{font-family:'Montserrat',sans-serif;font-weight:700;font-size:17px}
.info p{font-size:13px;line-height:19px;color:var(--text);margin-top:4px}
.form{left:540px;top:3740px;width:500px;height:330px;border:1px solid var(--line);padding:30px 30px}
.field{position:absolute;font-size:12px;color:#8a8f98;border-bottom:1px solid var(--line);height:34px;padding-top:8px}
.submit{position:absolute;right:30px;bottom:30px;width:120px;height:34px;background:var(--blue);color:var(--white)}

/* footer */
.site-footer{left:0;top:4150px;width:1200px;height:442px}
.footer-brand{left:0;top:4300px;width:1200px;display:flex;justify-content:center;align-items:center;gap:12px}
.footer-brand .brand-name{color:var(--yellow)}
.footer-nav{left:0;top:4418px;width:1200px;display:flex;justify-content:center;gap:36px;font-family:'Montserrat',sans-serif;font-weight:700;font-size:13px;color:var(--white)}
.footer-rule{left:96px;top:4470px;width:1008px;height:1px;background:#2c2c2c}
.copyright{left:96px;top:4500px;color:#aaa;font-size:12px}
.socials{left:990px;top:4494px;display:flex;gap:10px}
.socials span{width:28px;height:28px;border-radius:50%;background:var(--blue-bright)}
</style>
</head>
<body>

<header class="abs site-header">
  <div class="abs brand"><span class="dot"></span><span class="brand-name">PAST Q</span></div>
  <div class="abs pill phone-pill">
    <svg width="14" height="14" viewBox="0 0 24 24"><path fill="#fff" d="M6.6 10.8a15.2 15.2 0 0 0 6.6 6.6l2.2-2.2c.3-.3.7-.4 1-.2 1.1.4 2.3.6 3.6.6.6 0 1 .4 1 1V20c0 .6-.4 1-1 1A17 17 0 0 1 3 4c0-.6.4-1 1-1h3.5c.6 0 1 .4 1 1 0 1.3.2 2.5.6 3.6.1.3 0 .7-.2 1z"/></svg>
    (555) 014-2290
  </div>
  <nav class="abs main-nav">
    <span>HOME</span><span>ABOUT US</span><span>R.I.M.</span><span>CONCIERGE</span><span>RISE FURTHER</span><span>PAST Q+</span><span>TESTIMONIALS</span>
    <span class="contact-btn">CONTACT US</span>
  </nav>
</header>

<section class="abs hero" role="img" aria-label="Young woman on a zipline among forest trees, arms raised"></section>
<h1 class="abs heading hero-title">Welcome to<br>Life Changing Center</h1>
<p class="abs hero-text">The Journey starts in the himalayas to Everest Base Camp, where transformation happened for both of them, it was going Past Q(uarter) what they could see, comprehend and imagine.</p>
<span class="abs pill hero-btn">Get Started</span>
<svg class="abs hero-wave" viewBox="0 0 1200 170" preserveAspectRatio="none">
  <path d="M0 40 Q420 190 1200 60 L1200 170 L0 170Z" fill="#0b4fc4"/>
  <path d="M0 62 Q420 205 1200 80 L1200 170 L0 170Z" fill="#f5c518"/>
  <path d="M0 82 Q420 220 1200 100 L1200 170 L0 170Z" fill="#ffffff"/>
</svg>

<!-- about -->
<h2 class="abs heading welcome-title"><span class="mark"></span>Welcome to Past Q</h2>
<div class="abs welcome-copy">
  <p>Contrary to popular belief, Lorem Ipsum is not simply random text. It has roots in a piece of classical Latin literature from 45 BC, making it over 2000 years old. Ellis Varden, a Latin professor at Marlow Ridge College in Virginia, looked up one of the more obscure Latin words, consectetur, from a Lorem Ipsum passage, and going through the cites of the word in classical literature, discovered the undoubtable source.</p>
  <p>Lorem Ipsum comes from sections 1.10.32 and 1.10.33 of "de Finibus Bonorum et Malorum" (The Extremes of Good and Evil) by Aurelian, written in 45 BC. This book is a treatise on the theory of ethics, very popular during the Renaissance.</p>
</div>
<span class="abs pill read-btn">Read More</span>

<div class="abs accent" style="left:822px;top:978px;width:60px;height:6px"></div>
<div class="abs accent" style="left:586px;top:1360px;width:6px;height:66px"></div>
<div class="abs portrait portrait-a" role="img" aria-label="Smiling woman holding a dark umbrella outdoors"></div>
<div class="abs portrait portrait-b" role="img" aria-label="Businessman in a blue suit smiling in an office"></div>
<div class="abs arrow-tab" style="left:808px;top:1380px;background:var(--blue)"><svg width="18" height="12" viewBox="0 0 18 12"><path d="M0 6h15M10 1l5 5-5 5" stroke="#fff" stroke-width="2" fill="none"/></svg></div>
<div class="abs arrow-tab" style="left:1046px;top:1322px;background:var(--yellow)"><svg width="18" height="12" viewBox="0 0 18 12"><path d="M0 6h15M10 1l5 5-5 5" stroke="#1b1b1b" stroke-width="2" fill="none"/></svg></div>

<!-- consulting -->
<section class="abs consulting"></section>
<h2 class="abs heading consulting-title"><span class="mark"></span>Consulting</h2>

<div class="abs service" style="left:140px;top:1740px">
  <svg width="40" height="40" viewBox="0 0 40 40"><circle cx="20" cy="12" r="6" fill="none" stroke="#fff" stroke-width="2"/><path d="M8 34c0-7 5-12 12-12s12 5 12 12" fill="none" stroke="#fff" stroke-width="2"/></svg>
  <h3>Stewardship ascent</h3>
  <p>Focused guidance that lifts teams toward steady and lasting growth.</p>
  <span class="tab"><svg width="16" height="10" viewBox="0 0 16 10"><path d="M0 5h13M9 1l4 4-4 4" stroke="#fff" stroke-width="2" fill="none"/></svg></span>
</div>
<div class="abs service" style="left:400px;top:1740px">
  <svg width="40" height="40" viewBox="0 0 40 40"><circle cx="20" cy="20" r="14" fill="none" stroke="#fff" stroke-width="2"/><path d="M20 8v24M8 20h24" stroke="#fff" stroke-width="2"/></svg>
  <h3>Our program</h3>
  <p>A clear program shaped around your goals, pace and people.</p>
  <span class="tab"><svg width="16" height="10" viewBox="0 0 16 10"><path d="M0 5h13M9 1l4 4-4 4" stroke="#fff" stroke-width="2" fill="none"/></svg></span>
</div>
<div class="abs service" style="left:640px;top:1740px">
  <svg width="40" height="40" viewBox="0 0 40 40"><circle cx="20" cy="20" r="14" fill="none" stroke="#fff" stroke-width="2"/><circle cx="20" cy="20" r="6" fill="none" stroke="#fff" stroke-width="2"/><circle cx="20" cy="20" r="1.5" fill="#fff"/></svg>
  <h3>Focusing on companies</h3>
  <p>Practical support that helps companies align vision, teams and results.</p>
  <span class="tab"><svg width="16" height="10" viewBox="0 0 16 10"><path d="M0 5h13M9 1l4 4-4 4" stroke="#fff" stroke-width="2" fill="none"/></svg></span>
</div>
<div class="abs service" style="left:880px;top:1740px">
  <svg width="40" height="40" viewBox="0 0 40 40"><rect x="6" y="14" width="28" height="20" rx="2" fill="none" stroke="#fff" stroke-width="2"/><path d="M15 14V9h10v5" fill="none" stroke="#fff" stroke-width="2"/></svg>
  <h3>Business orientated</h3>
  <p>Strategies built for real business needs and measurable daily progress.</p>
  <span class="tab"><svg width="16" height="10" viewBox="0 0 16 10"><path d="M0 5h13M9 1l4 4-4 4" stroke="#fff" stroke-width="2" fill="none"/></svg></span>
</div>
<svg class="abs consult-wave" viewBox="0 0 1200 140" preserveAspectRatio="none">
  <path d="M0 130 Q600 -40 1200 110 L1200 140 L0 140Z" fill="#ffffff"/>
</svg>

<!-- packages -->
<div class="abs packages-title"><span class="mark"></span><h2 class="heading">Our Packages</h2></div>

<div class="abs plan" style="left:100px;top:2270px">
  <div class="plan-head">DAYBREAK</div>
  <div class="price"><sup>€</sup>9,99</div>
  <div class="per">EUROS PER MONTH</div>
  <ul class="features"><li>Webinars</li><li>Articles</li><li>Materials</li><li>Podcasts</li><li>Live sessions about coaching</li><li>Leadership</li><li>Transformation</li></ul>
  <span class="pill sign">Sign up</span>
</div>
<div class="abs plan" style="left:440px;top:2270px">
  <div class="plan-head">GRAB&amp;GO</div>
  <div class="price"><sup>€</sup>19,99</div>
  <div class="per">EUROS PER MONTH</div>
  <ul class="features"><li>Webinars</li><li>Articles</li><li>Materials</li><li>Podcasts</li><li>Live sessions about coaching</li><li>Leadership</li><li>Transformation</li></ul>
  <span class="pill sign">Sign up</span>
</div>
<div class="abs plan" style="left:780px;top:2270px">
  <div class="plan-head">SHIFT</div>
  <div class="price"><sup>€</sup>29,99</div>
  <div class="per">EUROS PER MONTH</div>
  <ul class="features"><li>Webinars</li><li>Articles</li><li>Materials</li><li>Podcasts</li><li>Live sessions about coaching</li><li>Leadership</li><li>Transformation</li></ul>
  <span class="pill sign">Sign up</span>
</div>

<!-- rise further -->
<svg class="abs yellow-band" viewBox="0 0 1200 860" preserveAspectRatio="none">
  <path d="M0 40 Q500 300 1200 0 L1200 860 L0 860Z" fill="#f7d447"/>
  <path d="M0 120 Q600 300 1200 60 L1200 860 L0 860Z" fill="#f5c518"/>
</svg>
<div class="abs rise-title"><span class="mark"></span><h2 class="heading">Rise Further</h2></div>

<div class="abs pillar" style="left:120px;top:3100px">
  <div class="photo" role="img" aria-label="Smiling woman working on a laptop" style="background:linear-gradient(160deg,#c9b49a,#8a6d55)"></div>
  <h3>Path renewal</h3>
  <div class="go"><svg width="16" height="10" viewBox="0 0 16 10"><path d="M0 5h13M9 1l4 4-4 4" stroke="#fff" stroke-width="2" fill="none"/></svg></div>
</div>
<div class="abs pillar" style="left:366px;top:3100px">
  <div class="photo" role="img" aria-label="Group of people at an indoor event" style="background:linear-gradient(160deg,#b7a58c,#5f5a52)"></div>
  <h3>Events</h3>
  <div class="go"><svg width="16" height="10" viewBox="0 0 16 10"><path d="M0 5h13M9 1l4 4-4 4" stroke="#fff" stroke-width="2" fill="none"/></svg></div>
</div>
<div class="abs pillar" style="left:612px;top:3100px">
  <div class="photo" role="img" aria-label="Hiker looking over a green mountain valley" style="background:linear-gradient(160deg,#a9c48c,#4d7a3c)"></div>
  <h3>Focusing on individuals</h3>
  <div class="go"><svg width="16" height="10" viewBox="0 0 16 10"><path d="M0 5h13M9 1l4 4-4 4" stroke="#fff" stroke-width="2" fill="none"/></svg></div>
</div>
<div class="abs pillar" style="left:858px;top:3100px">
  <div class="photo" role="img" aria-label="Business team meeting around a table" style="background:linear-gradient(160deg,#d0cabf,#6e6a66)"></div>
  <h3>Primarily life changing</h3>
  <div class="go"><svg width="16" height="10" viewBox="0 0 16 10"><path d="M0 5h13M9 1l4 4-4 4" stroke="#fff" stroke-width="2" fill="none"/></svg></div>
</div>

<!-- contact -->
<div class="abs contact-title"><span class="mark"></span><h2 class="heading">Get in Touch With Us</h2></div>

<div class="abs info" style="top:3810px">
  <svg width="22" height="28" viewBox="0 0 22 28"><path d="M11 0a10 10 0 0 0-10 10c0 8 10 18 10 18s10-10 10-18A10 10 0 0 0 11 0z" fill="#0b4fc4"/><circle cx="11" cy="10" r="4" fill="#fff"/></svg>
  <div><h4>Address</h4><p>12 Harbor Lane, Suite 4,<br>Brookfield 55210</p></div>
</div>
<div class="abs info" style="top:3900px">
  <svg width="24" height="18" viewBox="0 0 24 18"><rect width="24" height="18" rx="2" fill="#0b4fc4"/><path d="M1 2l11 8 11-8" stroke="#fff" stroke-width="2" fill="none"/></svg>
  <div><h4>Email Address</h4><p>info@pastq.example<br>admin@pastq.example</p></div>
</div>
<div class="abs info" style="top:3990px">
  <svg width="22" height="22" viewBox="0 0 24 24"><path fill="#0b4fc4" d="M6.6 10.8a15.2 15.2 0 0 0 6.6 6.6l2.2-2.2c.3-.3.7-.4 1-.2 1.1.4 2.3.6 3.6.6.6 0 1 .4 1 1V20c0 .6-.4 1-1 1A17 17 0 0 1 3 4c0-.6.4-1 1-1h3.5c.6 0 1 .4 1 1 0 1.3.2 2.5.6 3.6.1.3 0 .7-.2 1z"/></svg>
  <div><h4>Phone Number</h4><p>+1 (555) 014-2290<br>(555) 014-2291</p></div>
</div>

<form class="abs form">
  <span class="field" style="left:30px;top:30px;width:205px">Your Name</span>
  <span class="field" style="left:265px;top:30px;width:205px">Email Address</span>
  <span class="field" style="left:30px;top:90px;width:205px">Phone Number</span>
  <span class="field" style="left:265px;top:90px;width:205px">Subject</span>
  <span class="field" style="left:30px;top:150px;width:440px;height:80px">Your Message Goes Here</span>
  <span class="pill submit">Submit</span>
</form>

<!-- footer -->
<svg class="abs site-footer" viewBox="0 0 1200 442" preserveAspectRatio="none">
  <path d="M0 40 Q600 -20 1200 40 L1200 442 L0 442Z" fill="#f5c518"/>
  <path d="M0 52 Q600 -8 1200 52 L1200 442 L0 442Z" fill="#050505"/>
</svg>
<div class="abs footer-brand"><span class="mark"></span><span class="brand-name">PAST Q</span></div>
<nav class="abs footer-nav">
  <span>HOME</span><span>ABOUT US</span><span>R.I.M.</span><span>CONCIERGE</span><span>RISE FURTHER</span><span>PAST Q+</span><span>TESTIMONIALS</span>
</nav>
<div class="abs footer-rule"></div>
<p class="abs copyright">Copyright 2023 © Past Q. All Rights Reserved</p>
<div class="abs socials"><span></span><span></span><span></span><span></span></div>

</body>
</html>
```